WE RISE NOW - Personal Growth Seminar

The project is collaboration between Desmond Farrow and Marian Pelloway. It will combine the skills of both parties to launch an inspirational and motivation Personal Growth Seminar. We are looking for an e-flyer and a general design that we can use in our promotional work

The programme is a one day seminar which will show delegates how to

1) Kick start your life
2) Overcome obstacles and self sabotage
3) Take control of your future
4) Think bigger than you thought possible
5) Increase your confidence and self belief
6) Six steps to WE RISE NOW success

Our values for the seminar, that the eflyer should represent are:
Professional
Freedom
Nature (really important theme)
Fun
Honest
Balance
Integrity

We want to GRAB people's attention and then ENGAGE them into booking onto the seminar. We will send over details for the links to the seminar and phone numbers etc later, so they need to be incorporated. The seminar will be held in a hotel called The Hazelmere (nature and growth theme)

The one thing to remember is, to step back from the design and ask yourself would you book the seminar, based on what you see.

Our websites so you can see our current themes are www.marianpelloway.com and www.desmondfarrow.co.uk

Target Market(s)

Adults based in UK, between 25 and 50 years of age.

Industry/Entity Type

Hotel

Requirements
Must have
• Nature theme - growth
Fun but professional

Colours green but more vibrant like grass colour, nothing dull or washed out

Nice to have
• The picture will give you an idea but doesn't need to be used, it is just for guidance.

A Tree theme could be used - perhaps with the WE RISE NOW on the branches
Should not have
• Should not include cartoons

Gawdy colours or too much text

```html
<!DOCTYPE html>
<html lang="en">
<head>
<meta charset="utf-8">
<title>We Rise Now – One Day Seminar</title>
<link href="https://fonts.googleapis.com/css2?family=Fredericka+the+Great&family=Jost:wght@300;400&family=Pathway+Gothic+One&display=swap" rel="stylesheet">
<style>
  :root {
    --grass-deep: #1f6a12;
    --grass-mid: #3f9a22;
    --grass-light: #8fd14a;
    --leaf: #43a32c;
    --ink: #4a4a4a;
    --ink-soft: #5c5c5c;
    --paper: #ffffff;
    --silver: #eef0ea;
  }
  * { margin: 0; padding: 0; box-sizing: border-box; }
  html, body { width: 849px; height: 1200px; overflow: hidden; background: var(--paper); }
  .flyer { position: relative; width: 849px; height: 1200px; background: var(--paper); overflow: hidden; font-family: 'Jost', sans-serif; font-weight: 300; color: var(--ink); }
  .grass { position: absolute; left: 0; width: 849px; display: block; }
  .grass--top { top: 0; height: 460px; }
  .grass--bottom { top: 990px; height: 210px; }

  .title { position: absolute; left: 0; width: 849px; text-align: center; font-family: 'Fredericka the Great', serif; color: var(--silver); text-shadow: 0 3px 4px rgba(0,0,0,.35); }
  .title__main { top: 62px; font-size: 122px; line-height: 1; letter-spacing: 2px; }
  .title__sub { top: 222px; font-size: 78px; line-height: 1; }

  .pill { position: absolute; left: 41px; width: 768px; border-radius: 24px; }
  .pill--programme { top: 470px; height: 47px; background: var(--leaf); color: var(--paper); font-family: 'Pathway Gothic One', sans-serif; font-size: 29px; line-height: 47px; padding-left: 36px; }

  .outcomes { position: absolute; top: 530px; left: 0; width: 849px; text-align: center; font-size: 20.5px; line-height: 45px; }
  .dot { color: var(--leaf); padding: 0 4px; font-family: Arial, sans-serif; font-size: 20px; }
  .brand-inline { font-family: 'Fredericka the Great', serif; color: var(--leaf); font-size: 30px; }

  .rule { position: absolute; left: 41px; width: 768px; height: 1px; background: var(--leaf); }

  .venue { position: absolute; top: 678px; left: 0; width: 849px; text-align: center; font-size: 20.5px; line-height: 1.4; }
  .venue__name { font-family: 'Fredericka the Great', serif; color: var(--leaf); font-size: 40px; line-height: 1.1; }
  .venue__line { margin-top: 2px; line-height: 40px; }

  .speaker { position: absolute; }
  .portrait { position: absolute; width: 134px; height: 134px; border-radius: 50%; box-shadow: 2px 4px 8px rgba(0,0,0,.35); border: 3px solid var(--paper); }
  .portrait--desmond { left: 35px; top: 871px; background: radial-gradient(circle at 50% 45%, #c98f68 0%, #8a5a3c 50%, #2c3a44 100%); }
  .portrait--marian { left: 432px; top: 850px; background: radial-gradient(circle at 50% 40%, #d9cfc6 0%, #b89a87 55%, #7a6a60 100%); }
  .speaker__name { font-size: 23px; color: var(--ink); }
  .speaker__role { font-size: 16px; line-height: 30.5px; color: var(--ink-soft); }
  .speaker--desmond { left: 192px; top: 880px; }
  .speaker--marian { left: 595px; top: 858px; }
  .speaker--marian .speaker__name { margin-bottom: 2px; }
  .slogan { position: absolute; left: 192px; top: 1006px; font-family: 'Pathway Gothic One', sans-serif; font-size: 26px; line-height: 32px; color: var(--leaf); }

  .pill--web { top: 1124px; height: 42px; background: var(--paper); font-family: 'Pathway Gothic One', sans-serif; font-size: 28px; line-height: 42px; text-align: center; color: var(--leaf); }
  .pill--web .url { color: var(--ink); }
</style>
</head>
<body>
<main class="flyer">
  <svg class="grass grass--top" viewBox="0 0 849 460" role="img" aria-label="Close-up photograph of dewy green grass blades with soft bokeh light">
    <defs>
      <radialGradient id="topGrass" cx="0.35" cy="0.3" r="0.9">
        <stop offset="0" stop-color="#9fdc55"/>
        <stop offset="0.45" stop-color="#4fa82a"/>
        <stop offset="1" stop-color="#1d5f10"/>
      </radialGradient>
    </defs>
    <path d="M0 0 H849 V385 C700 370 560 395 420 430 C330 452 260 458 190 438 C120 418 60 380 0 350 Z" fill="url(#topGrass)"/>
  </svg>

  <h1 class="title title__main">we rise now</h1>
  <p class="title title__sub">one day seminar</p>

  <p class="pill pill--programme">The programme is a one day seminar which will show delegates how to:-</p>

  <p class="outcomes">
    Kick start your life <span class="dot">•</span> Overcome obstacles and self sabotage <span class="dot">•</span><br>
    Take control of your future <span class="dot">•</span> Think bigger than you thought possible <span class="dot">•</span><br>
    Increase your confidence and self belief <span class="dot">•</span> Six steps to <span class="brand-inline">we rise now</span> success
  </p>

  <div class="rule" style="top:669px"></div>

  <section class="venue">
    <p>The Seminar is to be held at</p>
    <p class="venue__name">the hazelmere hotel</p>
    <p class="venue__line">First line of the Address <span class="dot">•</span> Street Name <span class="dot">•</span> Area <span class="dot">•</span> Post code</p>
    <p class="venue__line">On Saturday <span class="dot">•</span> 00th <span class="dot">•</span> Month <span class="dot">•</span> 201</p>
  </section>

  <div class="rule" style="top:839px"></div>

  <svg class="grass grass--bottom" viewBox="0 0 849 210" role="img" aria-label="Photograph of sunlit green grass blades along the bottom edge">
    <defs>
      <linearGradient id="bottomGrass" x1="0" y1="0" x2="1" y2="1">
        <stop offset="0" stop-color="#6fbf3a"/>
        <stop offset="0.5" stop-color="#3f962a"/>
        <stop offset="1" stop-color="#1f6412"/>
      </linearGradient>
    </defs>
    <path d="M0 20 C90 30 160 70 290 74 C440 78 600 28 849 34 V210 H0 Z" fill="url(#bottomGrass)"/>
  </svg>

  <div class="portrait portrait--desmond" role="img" aria-label="Portrait photograph of Desmond Farrow"></div>
  <div class="speaker speaker--desmond">
    <p class="speaker__name">Desmond Farrow</p>
    <p class="speaker__role">Motivational speaker,<br>professional speaker,<br>inspirational speaker.</p>
  </div>
  <p class="slogan">Everything starts with “WeRise”</p>

  <div class="portrait portrait--marian" role="img" aria-label="Portrait photograph of Marian Pelloway"></div>
  <div class="speaker speaker--marian">
    <p class="speaker__name">Marian Pelloway</p>
    <p class="speaker__role">Change Speaker,<br>Communication Coach<br>and Hypnotherapist.</p>
  </div>

  <p class="pill pill--web">Visit our websites <span class="url">www.marianpelloway.com</span> and <span class="url">www.desmondfarrow.co.uk</span></p>
</main>
</body>
</html>
```